Aviation security consulting company needs a website

We need a website design for Brell Ostavik, and aviation security consulting company. Brell Ostavik (www.brellostavik.example) is an aviation security consulting company that works with government and industry stakeholders in over 60 countries on aviation security strategy, governance, and oversight at the regulatory and operational level.
Brell Ostavik is strongly internationally focused.
The website required should be simple, corporate, serious, and communicate professionalism, reliability and honesty. We are trying to give the company a feeling of being well established.
The attached files include the company logo, along with examples of company web page styles that we like.
The Brell Ostavik website need only be around five pages long (landing page, who we are, our services, our clients, contact), though don't feel limited to only five pages.
The existing website (www.brellostavik.example) was rushed and put together using Wix. We don't love the existing website as it looks too amateur, so don't use it as a template.
There is no requirement for any online sales tools to be included in the site. The site is purely informational, with the option of people making contact via email.

```html
<!DOCTYPE html>
<html lang="en">
<head>
<meta charset="utf-8">
<title>Brell Ostavik — Aviation Security Consulting</title>
<link href="https://fonts.googleapis.com/css2?family=Roboto:wght@400;500;700&family=Open+Sans:wght@400;600;700&family=Sacramento&display=swap" rel="stylesheet">
<style>
:root{
  --navy:#1f336a;
  --navy-deep:#1a2c5c;
  --blue:#1e6fc9;
  --blue-light:#2f9be3;
  --ink:#2a2a2a;
  --muted:#555a66;
  --paper:#ffffff;
  --soft:#f4f6f9;
  --accent:#2a7fd4;
  --teal:#2e9ad0;
  --footer-text:#aeb8d4;
}
*{margin:0;padding:0;box-sizing:border-box}
html,body{width:1200px;height:2715px;overflow:hidden;background:var(--paper)}
body{position:relative;font-family:"Open Sans",Arial,sans-serif;color:var(--ink)}
.abs{position:absolute}
/* top bar */
.topbar{left:0;top:0;width:1200px;height:36px;background:#fff;font-family:"Roboto",sans-serif;font-size:12px;color:#777}
.topbar span{position:absolute;top:11px}
.flag{display:inline-block;width:16px;height:10px;background:#3b5aa3;margin-right:5px;vertical-align:-1px}
.contact-btn{position:absolute;left:968px;top:8px;width:82px;height:20px;background:var(--navy);color:#fff;border-radius:3px;font-size:11px;font-weight:700;text-align:center;line-height:20px}
.social-dot{position:absolute;top:12px;width:11px;height:11px;border-radius:50%;background:var(--navy)}
/* nav */
.nav{left:0;top:36px;width:1200px;height:64px;background:var(--navy)}
.nav a{position:absolute;top:22px;color:#fff;text-decoration:none;font-family:"Roboto",sans-serif;font-size:15px;font-weight:500}
.logo{left:54px;top:36px;width:284px;height:76px;background:#fff;border-radius:0 0 6px 6px;box-shadow:0 2px 6px rgba(0,0,0,.15);z-index:3}
.logo-mark{position:absolute;left:12px;top:14px;width:44px;height:44px;background:var(--navy)}
.logo-name{position:absolute;left:66px;top:10px;font-family:"Roboto",sans-serif;font-weight:700;font-size:30px;color:var(--navy);letter-spacing:-.5px}
.logo-tag{position:absolute;left:68px;top:48px;font-family:"Roboto",sans-serif;font-size:12px;color:var(--navy);letter-spacing:1.2px}
/* hero */
.hero{left:0;top:100px;width:1200px;height:552px;background:linear-gradient(180deg,#4d6c8f 0%,#7b95ad 45%,#3b4350 78%,#1f2329 100%)}
.hero-title{left:0;top:250px;width:1200px;text-align:center;font-family:"Sacramento",cursive;font-size:92px;color:#fff;line-height:1}
.hero-sub{left:0;top:356px;width:1200px;text-align:center;font-family:"Roboto",sans-serif;font-weight:500;font-size:22px;line-height:33px;color:#fff}
.btn-solid{left:483px;top:449px;width:100px;height:31px;background:#fff;color:var(--accent);font-family:"Roboto",sans-serif;font-size:10px;font-weight:700;text-align:center;line-height:31px;border-radius:2px}
.btn-outline{left:617px;top:449px;width:107px;height:31px;border:1.5px solid #fff;color:#fff;font-family:"Roboto",sans-serif;font-size:10px;font-weight:700;text-align:center;line-height:28px;border-radius:2px}
.dot{top:613px;width:9px;height:9px;border-radius:50%;background:#fff}
/* stats */
.stats{left:0;top:652px;width:1200px;height:257px;background:linear-gradient(100deg,#1d4fa0 0%,#2d96e0 50%,#1d4fa0 100%);color:#fff;font-family:"Roboto",sans-serif}
.stat{position:absolute;top:20px;width:320px;text-align:center}
.stat h3{font-size:16px;font-weight:500}
.stat .num{font-size:42px;font-weight:700;margin-top:14px}
.stat p{font-size:11px;line-height:17px;margin-top:14px}
/* sections */
.section-title{left:0;width:1200px;text-align:center;font-family:"Roboto",sans-serif;font-weight:700;font-size:20px;color:var(--ink)}
.dotted{left:92px;width:1016px;border-top:2px dotted #8a93a8}
.about{left:0;top:909px;width:1200px;height:372px;background:var(--soft)}
.col{position:absolute;text-align:center;font-family:"Roboto",sans-serif}
.col h4{font-size:16px;font-weight:700;color:var(--ink)}
.col p{font-size:11.5px;line-height:18px;color:var(--muted);margin-top:10px;font-family:"Open Sans",sans-serif}
.col h4.highlight{color:#1f2fd0}
.plane-band{left:0;top:1281px;width:1200px;height:276px;background:linear-gradient(180deg,#8a4a1c 0%,#c9772c 45%,#e9a33d 75%,#b86824 100%)}
.clients{left:0;top:2027px;width:1200px;height:190px;background:var(--soft)}
.badge{position:absolute;top:20px;width:152px;height:150px}
.skyline-band{left:0;top:2208px;width:1200px;height:64px;background:linear-gradient(180deg,#f4f6f9 0%,#b9c2d6 55%,#1f336a 100%)}
.footer{left:0;top:2272px;width:1200px;height:443px;background:var(--navy);color:var(--footer-text);font-family:"Roboto",sans-serif}
.footer h5{position:absolute;font-size:17px;font-weight:700;color:#fff}
.footer .txt{position:absolute;font-size:12.5px;line-height:20px}
.footer .label{color:#fff;font-weight:400}
.social-row i{display:inline-block;width:11px;height:11px;border-radius:50%;background:var(--footer-text);margin-right:12px}
.field{position:absolute;left:333px;width:534px;background:#fff;border-radius:2px;color:#666;font-size:12px;padding:7px 14px}
.send{position:absolute;left:333px;top:284px;width:134px;height:31px;background:var(--teal);color:#fff;font-size:12px;font-weight:700;text-align:center;line-height:31px;border-radius:2px}
.fdivider{position:absolute;left:52px;top:380px;width:1096px;border-top:1px solid #3a4d82}
.copy{position:absolute;left:0;top:406px;width:1200px;text-align:center;font-size:12px}
.icon{display:block;margin:0 auto}
</style>
</head>
<body>

<div class="abs topbar">
  <span style="left:525px">&#9742; +1 800 555 0142</span>
  <span style="left:673px">&#9993; info@brellostavik.example</span>
  <span style="left:860px"><i class="flag"></i>English &#8964;</span>
  <div class="contact-btn">CONTACT US</div>
  <i class="social-dot" style="left:1074px"></i>
  <i class="social-dot" style="left:1110px"></i>
</div>

<div class="abs nav">
  <a style="left:507px">HOME</a>
  <a style="left:589px">WHO WE ARE</a>
  <a style="left:721px">OUR SERVICES</a>
  <a style="left:857px">OUR CLIENTS</a>
  <a style="left:985px">NEWS</a>
  <a style="left:1064px">CONTACTS</a>
</div>

<div class="abs logo">
  <div class="logo-mark"></div>
  <div class="logo-name">Brell Ostavik</div>
  <div class="logo-tag">aviation security consulting</div>
</div>

<div class="abs hero" role="img" aria-label="Photo of travellers silhouetted against an airport terminal window with an aircraft taking off"></div>
<div class="abs hero-title">Our Life's Work</div>
<div class="abs hero-sub">We Put Our Hearts and Souls into Making Every Project.<br>We Undertake the Very Best It Can Possibly Be.</div>
<div class="abs btn-solid">OUR SERVICES</div>
<div class="abs btn-outline">GO ON SURFING</div>
<i class="abs dot" style="left:578px;background:transparent;border:1px solid #fff"></i>
<i class="abs dot" style="left:595px"></i>
<i class="abs dot" style="left:612px"></i>

<div class="abs stats">
  <div class="stat" style="left:64px">
    <h3>Countries</h3><div class="num">60</div>
    <p>Brell Ostavik's experience and partnerships across all regions and sectors in 60 countries has enabled the company to complete projects of various sizes and specifications while maintaining high levels of efficiency and quality</p>
  </div>
  <div class="stat" style="left:440px">
    <h3>Satisfied Clients</h3><div class="num">100</div>
    <p>Given their satisfaction with our work, the majority of the clients have become our partners they turn to us as year after year with their Security Consulting</p>
  </div>
  <div class="stat" style="left:816px">
    <h3>Finished Projects</h3><div class="num">240</div>
    <p>Major sponsors of Brell Ostavik work have included government and public sector organizations, foundations and associations, international and local organizations, and private sector entities</p>
  </div>
</div>

<div class="abs about"></div>
<div class="abs section-title" style="top:934px">Aviation Security Consulting</div>
<div class="abs dotted" style="top:974px"></div>

<div class="col" style="left:59px;top:1014px;width:330px">
  <svg class="icon" width="80" height="80" viewBox="0 0 80 80"><path d="M4 22V4h72v72H4V58" fill="none" stroke="#1f336a" stroke-width="7"/><path d="M26 38h8v20h-8zM36 56V38l8-14c3 0 4 3 3 6l-2 6h12c3 0 4 3 3 5l-4 12c-1 2-2 3-4 3z" fill="none" stroke="#1f336a" stroke-width="2.5"/></svg>
  <h4 class="highlight" style="margin-top:22px">Who we are</h4>
  <p>Brell Ostavik is a full service aviation security consulting company with experience in over 60 countries. We work with government and industry stakeholders to deliver outstanding security outcomes at both a regulatory and operational level.</p>
</div>
<div class="col" style="left:424px;top:1014px;width:350px">
  <svg class="icon" width="80" height="80" viewBox="0 0 80 80"><path d="M4 22V4h72v72H4V58" fill="none" stroke="#1f336a" stroke-width="7"/><path d="M40 20c6 6 7 16 4 26h-8c-3-10-2-20 4-26zM36 46l-5 8h5M44 46l5 8h-5M38 54l2 6 2-6" fill="none" stroke="#1f336a" stroke-width="2.5"/><circle cx="40" cy="33" r="3" fill="none" stroke="#1f336a" stroke-width="2"/></svg>
  <h4 style="margin-top:22px">Our Mission</h4>
  <p>Brell Ostavik is a team of aviation security professionals that work toward delivering security services while upholding the highest standards of design, analysis and reporting. Our mission is to help set the industry in consulting services</p>
</div>
<div class="col" style="left:799px;top:1014px;width:350px">
  <svg class="icon" width="80" height="80" viewBox="0 0 80 80"><path d="M4 22V4h72v72H4V58" fill="none" stroke="#1f336a" stroke-width="7"/><path d="M28 20h18l8 8v32H28zM46 20v8h8M33 36h16M33 42h16M33 48h16" fill="none" stroke="#1f336a" stroke-width="2.5"/></svg>
  <h4 style="margin-top:22px">Our Vision</h4>
  <p>Our vision is to be a long-term preferred partner to our clients in the field of market security and business consulting. We are relentlessly focused on delivering exceptional value in provision of strategy, security and training</p>
</div>

<div class="abs plane-band" role="img" aria-label="Photo of an airliner silhouette taking off against an orange sunset sky"></div>

<div class="abs section-title" style="top:1568px">Our Services</div>
<div class="abs dotted" style="top:1605px"></div>

<div class="col" style="left:47px;top:1647px;width:170px">
  <svg class="icon" width="80" height="80" viewBox="0 0 80 80"><path d="M4 22V4h72v72H4V58" fill="none" stroke="#1f336a" stroke-width="7"/><path d="M40 20l16 6v12c0 10-7 18-16 22-9-4-16-12-16-22V26z" fill="none" stroke="#1f336a" stroke-width="2.5"/><path d="M33 40l5 5 10-10" fill="none" stroke="#1f336a" stroke-width="2.5"/></svg>
  <h4 style="margin-top:18px;line-height:24px">Civil Aviation<br>Authority</h4>
  <p>Aviation security regulatory agencies are required to navigate a plethora of conflicting domestic regulation, along with regional and international aviation security requirements.</p>
</div>
<div class="col" style="left:235px;top:1647px;width:170px">
  <svg class="icon" width="80" height="80" viewBox="0 0 80 80"><path d="M4 22V4h72v72H4V58" fill="none" stroke="#1f336a" stroke-width="7"/><path d="M26 18h28v44H26zM32 26h16v30H32zM40 26v30" fill="none" stroke="#1f336a" stroke-width="2.5"/><circle cx="40" cy="36" r="3" fill="#1f336a"/></svg>
  <h4 style="margin-top:18px;line-height:24px">Airport Operations<br>and Screening</h4>
  <p>Brell Ostavik can work with airports and airport designers to ensure security is incorporated in airport designs, and is maximised within existing airport environments.</p>
</div>
<div class="col" style="left:424px;top:1647px;width:170px">
  <svg class="icon" width="80" height="80" viewBox="0 0 80 80"><path d="M4 22V4h72v72H4V58" fill="none" stroke="#1f336a" stroke-width="7"/><path d="M24 20h6l8 32h18M36 28h14v18H40" fill="none" stroke="#1f336a" stroke-width="2.5"/><circle cx="40" cy="58" r="3.5" fill="none" stroke="#1f336a" stroke-width="2.5"/></svg>
  <h4 style="margin-top:18px;line-height:24px">Air Cargo / Handling<br>Agent</h4>
  <p>Air cargo security is seeing rapid changes, with issues such as pre-loading advanced cargo information, electronic consignment security declarations, and secure supply chains becoming more important.</p>
</div>
<div class="col" style="left:605px;top:1647px;width:180px">
  <svg class="icon" width="80" height="80" viewBox="0 0 80 80"><path d="M4 22V4h72v72H4V58" fill="none" stroke="#1f336a" stroke-width="7"/><path d="M40 18l10 5v10l-10 5-10-5V23zM30 38l10 5v10l-10 5-10-5V43zM50 38l10 5v10l-10 5-10-5V43z" fill="#1f336a"/></svg>
  <h4 style="margin-top:18px;line-height:24px">Capacity<br>Development</h4>
  <p>Every country is different, and while States must meet the same international standards, there is no 'one size fits all' approach. Each State must develop solutions that are sustainable in their economies.</p>
</div>
<div class="col" style="left:798px;top:1647px;width:170px">
  <svg class="icon" width="80" height="80" viewBox="0 0 80 80"><path d="M4 22V4h72v72H4V58" fill="none" stroke="#1f336a" stroke-width="7"/><path d="M56 22c2 2 0 5-3 8l-6 6 4 18-3 3-7-14-7 7 1 6-2 2-4-7-7-4 2-2 6 1 7-7-14-7 3-3 18 4 6-6c3-3 6-5 8-3z" fill="none" stroke="#1f336a" stroke-width="2.2"/></svg>
  <h4 style="margin-top:18px;line-height:24px">Airline<br>&nbsp;</h4>
  <p>Brell Ostavik can work with airlines on security issues such as security program development, station inspection and audit, strategic guidance, and change management.</p>
</div>
<div class="col" style="left:983px;top:1647px;width:170px">
  <svg class="icon" width="80" height="80" viewBox="0 0 80 80"><path d="M4 22V4h72v72H4V58" fill="none" stroke="#1f336a" stroke-width="7"/><path d="M34 22h24v18H34M36 40l-4 20M48 40l4 20" fill="none" stroke="#1f336a" stroke-width="2.5"/><circle cx="26" cy="28" r="4" fill="none" stroke="#1f336a" stroke-width="2.5"/><path d="M20 52V38h12l6-6" fill="none" stroke="#1f336a" stroke-width="2.5"/></svg>
  <h4 style="margin-top:18px;line-height:24px">Training<br>&nbsp;</h4>
  <p>Brell Ostavik has experienced aviation security trainers who can take participants through course material prepared by your organisation, or can develop training material tailored to your requirements.</p>
</div>

<div class="abs clients">
  <div class="badge" style="left:52px;background:#b81f1f"></div>
  <div class="badge" style="left:241px;background:#fff"><div style="margin:30px auto;width:92px;height:92px;border-radius:50%;background:#2c4ea0"></div></div>
  <div class="badge" style="left:429px;background:#fff"><div style="margin:62px auto;width:110px;height:26px;background:#c62828"></div></div>
  <div class="badge" style="left:619px;background:#1f4fa0"></div>
  <div class="badge" style="left:807px;background:#fff"><div style="margin:28px auto;width:96px;height:96px;border-radius:50%;background:#4a78c2"></div></div>
  <div class="badge" style="left:997px;background:#111"><div style="margin:12px;height:126px;background:#fff;border:3px solid #d87a20"></div></div>
</div>

<div class="abs skyline-band" role="img" aria-label="Illustration of a city and airport terminal skyline silhouette"></div>

<div class="abs footer">
  <h5 style="left:52px;top:56px">Contact Us</h5>
  <div class="txt" style="left:52px;top:96px;width:250px">Please feel free to contact us for any issue. Our staff is available to you from 9AM until 5PM on weekdays.</div>
  <div class="txt" style="left:52px;top:170px"><span class="label">Phone:</span> +1 (800) 555 0187</div>
  <div class="txt" style="left:52px;top:203px"><span class="label">Office:</span> 4120 Harlow Avenue, Northbridge</div>
  <div class="txt" style="left:52px;top:237px"><span class="label">Email:</span> hello@brellostavik.example</div>
  <div class="txt social-row" style="left:52px;top:276px"><i></i><i></i><i></i><i></i><i></i></div>

  <div class="field" style="top:54px;height:29px">Name *</div>
  <div class="field" style="top:106px;height:29px">Email *</div>
  <div class="field" style="top:157px;height:29px">Subject</div>
  <div class="field" style="top:208px;height:54px">Write Your Message Here...</div>
  <div class="send">SEND MESSAGE</div>

  <h5 style="left:896px;top:56px">About Team</h5>
  <div class="txt" style="left:896px;top:96px;width:250px">Enim congue blandit. Lorem ipsum dolor sit amet, consectetur adipiscing elit. Quisque consectetur interdum finibus. Vestibulum ante ipsum primis in faucibus orci. luctus et ultrices posuere.</div>
  <div class="txt" style="left:896px;top:212px;width:250px">Cubilia cras blandit finibus ipsum, id porttitor arcu volutpat a. Integer iaculis erat nec justo malesuada faucibus vel tempus sapien. Vivamus aliquam euismod tristique.</div>

  <div class="fdivider"></div>
  <div class="copy">Copyright 2020. All Rights Reserved by Brell Ostavik</div>
</div>

</body>
</html>
```